Bramwell Builders Web Site / Business Cards

Construction Company that specializes in Water and Fire Damage, Residential ReModels, Landscaping and Building ADU (Accessory Dwelling Unit)

Growing and changing families often need additional space, and a remodeling project can often provide that. Adding a new area, or repurposing an existing one can satisfy this requirement.

Other times, homeowners want to update the look in their kitchen or bathroom with more than just a change of cabinetry or vanity doors and drawers. Whatever your needs are, Bramwell Builders has skilled workers who are bonded and insured, and ready to make your dreams and visions a reality.

Target Market(s)

Home Owners

Industry/Entity Type

Construction Company

Contact Information for Business Card

Center Logo with our information on the corners

Back side to be Logo Only
Contact Info
SBRQ License # 5820914
info@bramwellbuildersca.example
www.bramwellbuildersca.example

Coding

Coded - Design and coding required

Number of Pages Required

5+ page

Font styles to use
Serif
Sans Serif

Requirements
Must have
• Using our Logo Colors
Home
About Us
Services
Projects / Portfolio
Contact Us
Nice to have
• Colors matching our Logo
Should not have
• Black because it doesnt match our logo

```html
<!DOCTYPE html>
<html lang="en">
<head>
<meta charset="utf-8">
<title>Bramwell Builders</title>
<link rel="stylesheet" href="https://fonts.googleapis.com/css2?family=Anton&family=Oswald:wght@500;600;700&family=Poppins:wght@300;400;500;600&family=Roboto+Condensed:wght@400;700&display=swap">
<style>
:root{
  --orange:#ff6a13;
  --orange-dark:#e85a08;
  --ink:#1f1f1f;
  --text:#555;
  --muted:#8a8a8a;
  --grey-bg:#f2f2f2;
  --white:#fff;
}
*{box-sizing:border-box;margin:0;padding:0}
html,body{width:1200px;height:4501px;overflow:hidden}
body{position:relative;background:var(--white);font-family:'Poppins',sans-serif;color:var(--text)}
.abs{position:absolute}
.center{text-align:center}
.head{font-family:'Oswald',sans-serif;font-weight:600;color:var(--ink);text-transform:uppercase;letter-spacing:.5px}
.head span{color:var(--orange)}
.btn{position:absolute;background:var(--orange);color:#fff;font-size:13px;font-weight:500;display:flex;align-items:center;justify-content:center;text-transform:uppercase}

/* hero */
.hero{left:0;top:0;width:1200px;height:713px;background:linear-gradient(180deg,#f4f4f4 0%,#e6e6e6 40%,#d2d2d2 80%,#b9b6b0 100%)}
.hero-photo{left:420px;top:280px;width:780px;height:433px;
  background:
    radial-gradient(ellipse 60% 30% at 55% 12%,#f6f6f4 0%,#ecebe8 60%,rgba(236,235,232,0) 100%),
    linear-gradient(180deg,rgba(0,0,0,0) 0%,rgba(0,0,0,0) 25%,#4a4540 32%,#3a3530 55%,#6e6a5a 72%,#8d8a78 86%,#b7b1a2 100%),
    linear-gradient(90deg,#dcdcdc 0%,#cfcfcf 100%)}
.logo-drop{left:150px;top:0;width:110px;height:131px}
.logo-text{left:160px;top:40px;width:90px;font-family:'Oswald',sans-serif;font-weight:700;font-size:15px;color:var(--ink);text-align:center;line-height:1.1}
.nav{left:550px;top:35px;display:flex;gap:24px;font-size:12px;color:var(--ink)}
.nav .active{color:var(--orange)}
.nav-bar{left:540px;top:26px;width:2px;height:28px;background:var(--orange)}
.phone-top{left:890px;top:24px;display:flex;align-items:center;gap:10px;font-family:'Roboto Condensed',sans-serif;font-weight:700;font-size:17px;color:var(--ink)}
.circle-ico{width:32px;height:32px;border-radius:50%;background:var(--orange);display:flex;align-items:center;justify-content:center}
.hero-title{left:160px;top:196px;font-family:'Anton',sans-serif;font-size:74px;line-height:78px;color:var(--ink);font-weight:400}
.hero-sub{left:161px;top:356px;font-family:'Oswald',sans-serif;font-weight:500;font-size:36px;color:var(--orange)}
.dots{left:164px;top:634px;display:flex;gap:9px}
.dots i{width:14px;height:14px;border-radius:50%;background:#fff;border:2px solid #ddd;display:block}
.dots i.on{border-color:var(--orange);background:var(--orange);box-shadow:inset 0 0 0 3px #fff}
.quote-box{left:694px;top:612px;width:346px;height:248px;background:var(--orange);color:#fff;text-align:center}
.quote-box h3{font-family:'Oswald',sans-serif;font-weight:600;font-size:31px;margin-top:32px}
.quote-box p{font-size:12.5px;line-height:21px;margin:16px 26px 0}
.quote-box .ghost{left:105px;top:168px;width:136px;height:36px;border:1px solid #fff;background:none}

/* welcome */
.sketch{left:0;top:713px;width:560px;height:560px;background:radial-gradient(ellipse at 40% 40%,#ececec 0%,#f6f6f6 50%,#fff 80%)}
.welcome-title{left:0;top:925px;width:1200px;font-size:33px}
.welcome-sub{left:0;top:978px;width:1200px;font-size:19px;color:#444}
.welcome-text{left:370px;top:1020px;width:460px;font-size:11.5px;line-height:21px;color:#666}
.feature{top:1150px;width:140px;text-align:center;font-family:'Roboto Condensed',sans-serif;font-size:14px;line-height:19px;color:var(--ink)}
.feature svg{display:block;margin:0 auto 22px}

/* services */
.services{left:0;top:1342px;width:1200px;height:713px;background:var(--grey-bg)}
.svc-title{left:0;top:1410px;width:1200px;font-size:33px}
.svc-sub{left:0;top:1462px;width:1200px;font-size:12.5px;line-height:21px;color:#555}
.svc-active{left:197px;top:1550px;width:254px;height:45px;background:var(--orange);color:#fff;font-size:14px;display:flex;align-items:center;padding-left:24px;gap:14px}
.svc-item{left:210px;font-size:14px;color:var(--ink);display:flex;align-items:center;gap:14px}
.svc-photo{left:512px;top:1550px;width:487px;height:290px;
  background:
    radial-gradient(ellipse 30% 35% at 55% 35%,#a0643a 0%,#8a5a36 50%,rgba(138,90,54,0) 100%),
    linear-gradient(180deg,#d9dde2 0%,#c7ccd0 18%,#8c8883 35%,#77736e 65%,#5f6e4a 85%,#4e5e3c 100%)}
.svc-card{left:512px;top:1796px;width:412px;height:120px;background:#fff;padding:30px 0 0 41px}
.svc-card h4{font-family:'Roboto Condensed',sans-serif;font-size:17px;color:var(--ink)}
.svc-card p{font-size:11px;line-height:20px;color:#777;margin-top:8px;width:300px}
.svc-arrow{left:897px;top:1829px;width:52px;height:52px;border-radius:50%;border:2px solid var(--orange);background:#fff;display:flex;align-items:center;justify-content:center}

/* stats */
.stat{width:195px;height:112px;background:var(--orange);color:#fff;display:flex;align-items:center;padding-left:14px;gap:10px;box-shadow:0 6px 14px rgba(0,0,0,.08)}
.stat b{display:block;font-family:'Oswald',sans-serif;font-weight:500;font-size:32px;line-height:34px}
.stat small{font-size:12px}

/* projects */
.proj-title{left:0;top:2212px;width:1200px;font-size:33px}
.proj-sub{left:0;top:2260px;width:1200px;font-size:12px;color:#444}
.tile{position:absolute}

/* contact strip */
.cta-title{left:0;top:3082px;width:1200px;font-family:'Oswald',sans-serif;font-weight:600;font-size:33px;color:var(--ink)}
.cta-title span{color:var(--orange)}
.cta-phone{left:0;top:3190px;width:1200px;font-size:28px;color:#444;letter-spacing:1px}

/* testimonial */
.testi{left:0;top:3352px;width:1200px;height:376px;background:linear-gradient(180deg,#ff7a2a 0%,var(--orange) 60%,#f36510 100%)}
.testi-title{left:0;top:3422px;width:1200px;font-size:33px;color:#fff}
.testi-text{left:340px;top:3486px;width:520px;font-size:13.5px;line-height:24px;color:#fff}
.testi-name{left:0;top:3610px;width:1200px;color:#fff;font-size:14px}
.testi-role{left:0;top:3636px;width:1200px;color:#ffe1cd;font-size:11px}
.avatar{left:544px;top:3672px;width:112px;height:112px;border-radius:50%;background:linear-gradient(180deg,#3a3634 0%,#c9b3a6 45%,#e8e2de 100%);border:4px solid #fff}

/* contact */
.contact-title{left:0;top:3852px;width:1200px;font-family:'Oswald',sans-serif;font-weight:600;font-size:33px;color:var(--ink)}
.contact-title span{color:var(--orange)}
.contact-sub{left:0;top:3902px;width:1200px;font-size:12px;color:#444}
.info{left:282px;display:flex;gap:26px;font-size:11.5px;line-height:19px;color:#555}
.info svg{flex:none}
.map{left:611px;top:3960px;width:360px;height:263px;background:linear-gradient(135deg,#ecebe6 0%,#f5f3ee 45%,#eef1e6 70%,#e2eaee 100%);border:1px solid #e3e3e3}

/* footer */
.footer{left:0;top:4282px;width:1200px;height:219px;background:var(--orange)}
.foot-logo{left:0;top:4345px;width:1200px;font-family:'Oswald',sans-serif;font-weight:700;font-size:24px;color:var(--ink)}
.socials{left:522px;top:4409px;display:flex;gap:8px}
.socials i{display:block;width:30px;height:30px;border:2px solid #fff;transform:rotate(45deg);margin:4px}
.copy{left:0;top:4452px;width:1200px;font-size:11px;color:#fff}
</style>
</head>
<body>

<!-- Hero -->
<div class="abs hero" role="img" aria-label="Misty grey mountain backdrop"></div>
<div class="abs hero-photo" role="img" aria-label="Modern dark timber house with white gabled roof on a rocky hillside"></div>
<svg class="abs logo-drop" viewBox="0 0 110 131"><polygon points="0,0 110,0 110,80 55,131 0,80" fill="#fff"/></svg>
<div class="abs logo-text">BRAMWELL<br><span style="font-size:9px;letter-spacing:1px;font-weight:500">BUILDERS</span></div>
<div class="abs nav-bar"></div>
<nav class="abs nav"><span class="active">Home</span><span>Company</span><span>Projects</span><span>Services</span><span>Contact</span></nav>
<div class="abs phone-top"><span class="circle-ico"><svg width="16" height="16" viewBox="0 0 24 24"><path fill="#fff" d="M6.6 10.8a15 15 0 0 0 6.6 6.6l2.2-2.2c.3-.3.7-.4 1-.2 1.1.4 2.3.6 3.6.6.6 0 1 .4 1 1V20c0 .6-.4 1-1 1A17 17 0 0 1 3 4c0-.6.4-1 1-1h3.5c.6 0 1 .4 1 1 0 1.3.2 2.5.6 3.6.1.3 0 .7-.2 1z"/></svg></span>1 555 302 7164</div>
<h1 class="abs hero-title">The Best<br>Choice</h1>
<div class="abs hero-sub">Because We Deliver</div>
<div class="btn" style="left:161px;top:419px;width:138px;height:39px">Get a Quote</div>
<div class="abs dots"><i class="on"></i><i></i><i></i><i></i></div>
<div class="abs quote-box">
  <h3>Have Any Project ?</h3>
  <p>Construction Company that specializes in Water and Fire Damage, Residential ReModels, Landscaping and Building ADU.</p>
  <div class="btn ghost">Get a Quote</div>
</div>

<!-- Welcome -->
<div class="abs sketch" role="img" aria-label="Faint architectural blueprint sketch with drafting compass"></div>
<h2 class="abs head center welcome-title">Welcome to <span>Bramwell</span></h2>
<div class="abs center welcome-sub">We Deliver Landmark Projects</div>
<p class="abs center welcome-text">We are rethoric question ran over her cheek When she reached the first hills of the Italic Mountains, she had a last view back on the skyline of her hometown Bookmarksgrove, the headline of Alphabet Village and the subline of her own road, the Line Lane.</p>

<div class="abs feature" style="left:262px"><svg width="52" height="52" viewBox="0 0 52 52"><polygon points="26,4 32,20 49,20 35,30 40,47 26,37 12,47 17,30 3,20 20,20" fill="none" stroke="#222" stroke-width="2"/><polygon points="20,24 12,44 26,34" fill="var(--orange)"/></svg>We've Reputation<br>For Excellence</div>
<div class="abs feature" style="left:437px"><svg width="64" height="52" viewBox="0 0 64 52"><path d="M6 18 L20 10 L32 18 L44 10 L58 18 L50 32 L38 42 L26 40 L14 32 Z" fill="none" stroke="#222" stroke-width="2"/><path d="M24 26 L32 20 L40 26" fill="none" stroke="var(--orange)" stroke-width="3"/></svg>We Build<br>Partnerships</div>
<div class="abs feature" style="left:613px"><svg width="52" height="52" viewBox="0 0 52 52"><path d="M8 24 h8 v22 h-8 z" fill="var(--orange)"/><path d="M16 24 L26 6 c4 0 5 3 4 7 l-2 8 h14 c3 0 5 3 4 6 l-4 15 c-1 3-3 4-6 4 H16" fill="none" stroke="#222" stroke-width="2"/></svg>Guided By<br>Commitment</div>
<div class="abs feature" style="left:788px"><svg width="60" height="52" viewBox="0 0 60 52"><circle cx="30" cy="14" r="7" fill="none" stroke="#222" stroke-width="2"/><circle cx="14" cy="20" r="6" fill="none" stroke="#222" stroke-width="2"/><circle cx="46" cy="20" r="6" fill="none" stroke="#222" stroke-width="2"/><path d="M18 46 c0-12 24-12 24 0" fill="var(--orange)"/><path d="M4 44 c0-10 16-10 16-4 M40 40 c0-6 16-6 16 4" fill="none" stroke="#222" stroke-width="2"/></svg>A Team of<br>Professionals</div>

<!-- Services -->
<div class="abs services"></div>
<h2 class="abs head center svc-title">Our <span>Services</span></h2>
<p class="abs center svc-sub">Construction Company that specializes in Water and Fire Damage,<br>Residential ReModels, Landscaping and Building ADU.</p>
<div class="abs svc-active"><svg width="16" height="14" viewBox="0 0 16 14"><path d="M1 13h14M3 13V5h10v8M2 5l6-4 6 4" fill="none" stroke="#fff" stroke-width="1.6"/></svg>Home Construction</div>
<div class="abs svc-item" style="top:1631px"><svg width="16" height="14" viewBox="0 0 16 14"><path d="M1 13h14M3 13V5h10v8M2 5l6-4 6 4" fill="none" stroke="var(--orange)" stroke-width="1.6"/></svg>Building Remodeling</div>
<div class="abs svc-item" style="top:1677px"><svg width="16" height="14" viewBox="0 0 16 14"><path d="M1 13h14M3 13V5h10v8M2 5l6-4 6 4" fill="none" stroke="var(--orange)" stroke-width="1.6"/></svg>Interior Design</div>
<div class="abs svc-item" style="top:1722px"><svg width="16" height="14" viewBox="0 0 16 14"><path d="M1 13h14M3 13V5h10v8M2 5l6-4 6 4" fill="none" stroke="var(--orange)" stroke-width="1.6"/></svg>Exterior Design</div>
<div class="abs svc-item" style="top:1768px"><svg width="16" height="14" viewBox="0 0 16 14"><path d="M1 13h14M3 13V5h10v8M2 5l6-4 6 4" fill="none" stroke="var(--orange)" stroke-width="1.6"/></svg>Renovation</div>
<div class="abs svc-item" style="top:1813px"><svg width="16" height="14" viewBox="0 0 16 14"><path d="M1 13h14M3 13V5h10v8M2 5l6-4 6 4" fill="none" stroke="var(--orange)" stroke-width="1.6"/></svg>Safety Management</div>
<div class="abs svc-photo" role="img" aria-label="Two-storey grey stucco house with timber gable porch"></div>
<div class="abs svc-card"><h4>Home Construction</h4><p>Lorem Ipsum is simply dummy text of the printing and typesetting this Lorem ipsum has.</p></div>
<div class="abs svc-arrow"><svg width="24" height="16" viewBox="0 0 24 16"><path d="M2 8h19M14 2l7 6-7 6" fill="none" stroke="#222" stroke-width="2.2"/></svg></div>

<!-- Stats -->
<div class="abs stat" style="left:187px;top:2007px"><svg width="44" height="40" viewBox="0 0 44 40"><rect x="3" y="4" width="30" height="30" fill="none" stroke="#fff" stroke-width="2"/><path d="M8 12h20M8 18h20M8 24h12M26 34l14-14" stroke="#fff" stroke-width="2"/></svg><div><b>53</b><small>Total Projects</small></div></div>
<div class="abs stat" style="left:398px;top:2014px;height:119px"><svg width="44" height="40" viewBox="0 0 44 40"><circle cx="22" cy="14" r="9" fill="none" stroke="#fff" stroke-width="2"/><path d="M6 38c0-12 32-12 32 0" fill="none" stroke="#fff" stroke-width="2"/></svg><div><b>371</b><small>Staff Members</small></div></div>
<div class="abs stat" style="left:608px;top:2007px"><svg width="44" height="40" viewBox="0 0 44 40"><path d="M3 10h24l6 4h8l-3 10-8 6-6-2-4 4-6-6-8-2-3-8z" fill="none" stroke="#fff" stroke-width="2"/></svg><div><b>15</b><small>Working In States</small></div></div>
<div class="abs stat" style="left:818px;top:2014px;height:119px"><svg width="44" height="40" viewBox="0 0 44 40"><circle cx="26" cy="16" r="12" fill="none" stroke="#fff" stroke-width="2"/><path d="M26 9v7l5 4M4 36l12-12" stroke="#fff" stroke-width="2" fill="none"/></svg><div><b>2600</b><small>Hours For Work</small></div></div>

<!-- Projects -->
<h2 class="abs head center proj-title">Recent <span>Projects</span></h2>
<div class="abs center proj-sub">Bramwell Builders Work</div>
<div class="tile" style="left:161px;top:2397px;width:283px;height:187px;background:linear-gradient(180deg,#f48a44 0%,#ee7a30 35%,#d9601a 70%,#c8550f 100%)" role="img" aria-label="Timber-framed interior in orange overlay"></div>
<div class="tile" style="left:161px;top:2598px;width:283px;height:337px;background:linear-gradient(180deg,#7f95b4 0%,#a3b2c6 22%,#6b5a4e 40%,#d9d6cf 58%,#4c4a48 78%,#7f8a6a 100%)" role="img" aria-label="Two-storey brick and white colonial house"></div>
<div class="tile" style="left:459px;top:2329px;width:282px;height:202px;background:linear-gradient(90deg,#1e1e1e 0%,#2b2b2b 28%,#e9e4da 42%,#d2c6b2 62%,#c7b79c 80%,#efe9de 100%)" role="img" aria-label="Built-in shelving and timber wardrobe interior"></div>
<div class="tile" style="left:459px;top:2547px;width:282px;height:285px;background:linear-gradient(180deg,#c5c8cc 0%,#a9adb1 35%,#2a2a2a 52%,#f0dcb0 62%,#3a3a3a 74%,#6f7a5d 100%)" role="img" aria-label="Modern two-storey house at dusk with lit windows"></div>
<div class="tile" style="left:459px;top:2846px;width:282px;height:187px;background:linear-gradient(90deg,#e2d4bd 0%,#f5f2ec 30%,#e6dfd4 55%,#7f9a62 80%,#efebe4 100%)" role="img" aria-label="Light living room with sofa and plants"></div>
<div class="tile" style="left:756px;top:2397px;width:284px;height:337px;background:linear-gradient(180deg,#6f9ccc 0%,#9cbbe0 25%,#d9d2c4 45%,#6d5c4c 62%,#b79f7f 80%,#9f9f9a 100%)" role="img" aria-label="Modern stucco and stone house entrance"></div>
<div class="tile" style="left:756px;top:2748px;width:284px;height:187px;background:linear-gradient(180deg,#f4f5f6 0%,#dfe6ec 30%,#c8d3dc 55%,#f2f2f0 75%,#a99c8b 100%)" role="img" aria-label="Bright white kitchen with ceiling fan"></div>

<!-- Call to action -->
<h2 class="abs center cta-title">Have Any <span>Project ?</span></h2>
<svg class="abs" style="left:576px;top:3138px" width="48" height="48" viewBox="0 0 48 48"><circle cx="24" cy="24" r="22" fill="var(--orange)" stroke="#ffd2b5" stroke-width="3"/><path fill="#fff" d="M18.6 22.3a11 11 0 0 0 5 5l1.7-1.6c.2-.2.5-.3.8-.2.8.3 1.7.4 2.7.4.4 0 .8.4.8.8v2.6c0 .5-.4.8-.8.8A12.8 12.8 0 0 1 16 17.3c0-.4.3-.8.8-.8h2.6c.5 0 .8.4.8.8 0 1 .2 1.9.4 2.7.1.3 0 .6-.2.8z"/></svg>
<div class="abs center cta-phone">555-302-7164</div>
<div class="btn" style="left:540px;top:3237px;width:120px;height:35px;font-size:11px">Get a Quote</div>

<!-- Testimonial -->
<div class="abs testi" role="img" aria-label="House facade behind an orange overlay"></div>
<h2 class="abs head center testi-title" style="color:#fff">What Our Client Say</h2>
<svg class="abs" style="left:164px;top:3522px" width="20" height="30" viewBox="0 0 20 30"><path d="M16 2L4 15l12 13" fill="none" stroke="#fff" stroke-width="2"/></svg>
<svg class="abs" style="left:1004px;top:3522px" width="20" height="30" viewBox="0 0 20 30"><path d="M4 2l12 13L4 28" fill="none" stroke="#fff" stroke-width="2"/></svg>
<p class="abs center testi-text">"Bramwell Builders is one of the best General contractors we've worked with. The entire team tactfully delivered a project of Exceptional Quality while staying on Schedule and under budget. We hope to work with Bramwell again in the Near Future!"</p>
<div class="abs center testi-name">— &nbsp;Renata Solis</div>
<div class="abs center testi-role">Project Manager</div>
<div class="abs avatar" role="img" aria-label="Client portrait"></div>

<!-- Contact -->
<h2 class="abs center contact-title">Contact <span>Us</span></h2>
<div class="abs center contact-sub">If you have an any Question For Contact Us Today !</div>
<div class="abs info" style="top:3960px"><svg width="28" height="28" viewBox="0 0 28 28"><rect x="5" y="5" width="18" height="18" transform="rotate(45 14 14)" fill="none" stroke="var(--orange)" stroke-width="1.5"/><path d="M14 8a4 4 0 0 1 4 4c0 3-4 7-4 7s-4-4-4-7a4 4 0 0 1 4-4z" fill="var(--orange)"/></svg><span>412 W Alder Crest Ave Fairhollow,<br>CA 90000</span></div>
<div class="abs info" style="top:4014px"><svg width="28" height="28" viewBox="0 0 28 28"><rect x="5" y="5" width="18" height="18" transform="rotate(45 14 14)" fill="none" stroke="var(--orange)" stroke-width="1.5"/><path fill="var(--orange)" d="M11 12.5a7 7 0 0 0 4.5 4.5l1.3-1.3c.2-.2.4-.2.6-.1.6.2 1.2.3 1.9.3v2.5c-5 0-9-4-9-9h2.5c0 .7.1 1.3.3 1.9.1.2 0 .4-.1.6z"/></svg><span>555-418-2093<br>555-302-7164 (office)</span></div>
<div class="abs info" style="top:4070px"><svg width="28" height="28" viewBox="0 0 28 28"><rect x="5" y="5" width="18" height="18" transform="rotate(45 14 14)" fill="none" stroke="var(--orange)" stroke-width="1.5"/><rect x="10" y="9" width="8" height="10" fill="var(--orange)"/></svg><span style="padding-top:5px">555-302-7188</span></div>
<div class="abs info" style="top:4108px"><svg width="28" height="28" viewBox="0 0 28 28"><rect x="5" y="5" width="18" height="18" transform="rotate(45 14 14)" fill="none" stroke="var(--orange)" stroke-width="1.5"/><rect x="9" y="10" width="10" height="8" fill="var(--orange)"/><path d="M9 10l5 4 5-4" stroke="#fff" fill="none"/></svg><span style="padding-top:5px">hello@bramwellbuildersca.example</span></div>
<div class="abs info" style="top:4146px"><svg width="28" height="28" viewBox="0 0 28 28"><rect x="5" y="5" width="18" height="18" transform="rotate(45 14 14)" fill="none" stroke="var(--orange)" stroke-width="1.5"/><circle cx="14" cy="14" r="5" fill="none" stroke="var(--orange)" stroke-width="1.5"/><path d="M14 11v3h2" stroke="var(--orange)" fill="none"/></svg><span>Mon–Fri: 10:00 – 16:00<br>Sat: 12:00 – 15:00<br>Sunday &amp; holidays: 09:00 – 12:00</span></div>
<div class="abs map" role="img" aria-label="Street map showing the office location"></div>

<!-- Footer -->
<div class="abs footer"></div>
<div class="abs center foot-logo">BRAMWELL<div style="font-size:10px;letter-spacing:2px;font-weight:500">BUILDERS</div></div>
<div class="abs socials"><i></i><i></i><i></i><i></i></div>
<div class="abs center copy">©Bramwell Builders -2020 All rights reserved.</div>

</body>
</html>
```